Kestrel Bridge Consulting (KBC) Business Card Design

I would like to create double-sided business cards that contain:
1) Name: Derek Molvane
2) Phone Number: +1 (555) 218-4907
3) Email: Derek.Molvane@KestrelBridgeConsulting.example
4) Website: KestrelBridgeConsulting.example

I would like to include my logo and a color scheme similar to the Varnholt Grand Prix Ostera squad color scheme (black, silver, greenish-blue – but can also include regular blue)

What we do: Our company develops and delivers innovative and pragmatic information technology and cybersecurity risk and compliance solutions for organizations in the commercial market as well as the federal, and state/local sectors.

```html
<!DOCTYPE html>
<html lang="en">
<head>
<meta charset="utf-8">
<title>Kestrel Bridge Consulting — Business Card</title>
<link rel="stylesheet" href="https://fonts.googleapis.com/css2?family=Exo+2:wght@300;400;700&display=swap">
<style>
  :root {
    --backdrop: #e6e6e6;
    --card-light-top: #f4f4f4;
    --card-light-bottom: #d9d9d9;
    --card-dark: #0c0c0c;
    --ink: #161616;
    --paper: #ffffff;
    --teal: #16a3a0;
    --divider-dark: #1a1a1a;
    --divider-light: #d8d8d8;
  }
  html, body {
    margin: 0;
    padding: 0;
    width: 1200px;
    height: 1200px;
    overflow: hidden;
    background: var(--backdrop);
  }
  .card-sheet {
    display: block;
    width: 1200px;
    height: 1200px;
  }
  .wordmark {
    font-family: "Exo 2", sans-serif;
    font-weight: 400;
    letter-spacing: 0.5px;
  }
  .wordmark--front { fill: var(--ink); font-size: 33px; }
  .wordmark--back { fill: var(--paper); font-size: 22px; }
  .web-address {
    font-family: "Exo 2", sans-serif;
    font-weight: 400;
    font-variant: small-caps;
    fill: var(--paper);
    font-size: 21px;
    letter-spacing: 1px;
  }
  .person-name {
    font-family: "Exo 2", sans-serif;
    fill: var(--paper);
    font-size: 29px;
    letter-spacing: 2px;
  }
  .person-name__first { font-weight: 300; }
  .person-name__last { font-weight: 700; }
  .contact-line {
    font-family: "Exo 2", sans-serif;
    font-weight: 400;
    font-variant: small-caps;
    fill: var(--paper);
    font-size: 18px;
    letter-spacing: 0.8px;
  }
</style>
</head>
<body>
<svg class="card-sheet" viewBox="0 0 1000 1000" xmlns="http://www.w3.org/2000/svg" role="group" aria-label="Business card, front and back">
  <defs>
    <linearGradient id="front-surface" x1="0" y1="0" x2="0" y2="1">
      <stop offset="0" stop-color="var(--card-light-top)"/>
      <stop offset="1" stop-color="var(--card-light-bottom)"/>
    </linearGradient>
    <clipPath id="front-shape">
      <path d="M205 65 H805 Q875 65 875 135 L852 432 Q848 475 800 475 H250 Q205 475 196 432 L130 145 Q120 65 205 65 Z"/>
    </clipPath>
    <clipPath id="back-shape">
      <path d="M210 540 H800 Q878 540 872 610 L822 915 Q814 958 765 958 H250 Q198 958 190 915 L130 615 Q122 540 210 540 Z"/>
    </clipPath>
  </defs>

  <!-- Front side -->
  <g class="card card--front">
    <g clip-path="url(#front-shape)">
      <rect class="card__surface" x="100" y="50" width="800" height="450" fill="url(#front-surface)"/>
      <rect class="card__base-band" x="100" y="412" width="800" height="80" fill="var(--card-dark)"/>
      <rect class="accent-tab" x="100" y="412" width="140" height="11" fill="var(--teal)"/>
      <rect class="accent-rule" x="240" y="422" width="660" height="2" fill="var(--teal)"/>
    </g>
    <circle class="brand-dot" cx="340" cy="248" r="40" fill="var(--teal)"/>
    <rect class="brand-divider" x="427" y="196" width="2" height="102" fill="var(--divider-dark)"/>
    <text class="wordmark wordmark--front">
      <tspan x="440" y="226">KESTREL</tspan>
      <tspan x="440" y="258">BRIDGE</tspan>
      <tspan x="440" y="290">CONSULTING</tspan>
    </text>
    <text class="web-address" x="330" y="457" textLength="450" lengthAdjust="spacingAndGlyphs">KestrelBridgeConsulting.example</text>
  </g>

  <!-- Back side -->
  <g class="card card--back">
    <g clip-path="url(#back-shape)">
      <rect class="card__surface" x="100" y="520" width="800" height="460" fill="var(--card-dark)"/>
      <rect class="accent-tab" x="100" y="764" width="80" height="10" fill="var(--teal)"/>
      <rect class="accent-rule" x="180" y="764" width="720" height="1.5" fill="var(--teal)"/>
      <rect class="accent-tab" x="100" y="843" width="83" height="10" fill="var(--teal)"/>
      <rect class="accent-rule" x="183" y="852" width="640" height="1.5" fill="var(--teal)"/>
    </g>
    <circle class="brand-dot" cx="295" cy="638" r="30" fill="var(--teal)"/>
    <rect class="brand-divider" x="356" y="597" width="1.5" height="72" fill="var(--divider-light)"/>
    <text class="wordmark wordmark--back">
      <tspan x="365" y="618">KESTREL</tspan>
      <tspan x="365" y="642">BRIDGE</tspan>
      <tspan x="365" y="666">CONSULTING</tspan>
    </text>
    <text class="person-name" x="238" y="742"><tspan class="person-name__first">DEREK</tspan> <tspan class="person-name__last">MOLVANE</tspan></text>
    <text class="contact-line contact-line--phone" x="238" y="788">+1 (555) 218-4907</text>
    <text class="contact-line contact-line--email" x="238" y="813" textLength="545" lengthAdjust="spacingAndGlyphs">Derek.Molvane@KestrelBridgeConsulting.example</text>
    <text class="contact-line contact-line--web" x="238" y="838" textLength="395" lengthAdjust="spacingAndGlyphs">KestrelBridgeConsulting.example</text>
  </g>
</svg>
</body>
</html>
```